"Your Golden Years Start Tomorrow!" book cover for 80 page or so book.

Need a book cover that stands out on Bookvale, so highly engaging colors, need to reflect optimism, hope and determination. Go to Bookvale, type my name in and see the covers for the three other books I had written.

There's a lot of negativity and fear for Americans looking at retirement. Yet, they don't need that fear, my book tells them why they can be confident in their ability to retire.

There will be NO spine writing for the book, too small.

Target Market(s)

stressed out people in their 50s and 60s. This book appeals to working people, not high end, wealthy types.

Industry/Entity Type

Financial Planning

Colors

Designer to choose colors to be used in the design.

Requirements
Must have
• Needs to reflect simplicity in action.
• Please spell out my full name, MARK DELVORTH, at the bottom of the cover.
Nice to have
• if there is anyway to put a picture of an RV (Recreational Vehicle) that would be great.
Should not have
• Do NOT want to be the stodgy, typical financial planning literature out there. No guy in a suit and tie. No one sitting on a beach.
• Do not want my face on the cover either. (On the back yes.)

```html
<!DOCTYPE html>
<html lang="en">
<head>
<meta charset="utf-8">
<title>Your Golden Years Start Tomorrow! — Book Cover</title>
<link rel="stylesheet" href="https://fonts.googleapis.com/css2?family=Tinos:wght@700&family=Cinzel:wght@500&family=Arimo:wght@400;700&display=swap">
<style>
  :root {
    --stage: #3a3a3a;
    --paper: #ffffff;
    --title-blue: #0b4f8a;
    --author-teal: #0f7a78;
    --link-teal: #2aa9c4;
    --ink: #1a1a1a;
    --rule-blue: #2b7fd0;
    --photo-teal: #33b3c9;
    --art-silver: #b9bec4;
    --art-mint: #62d1bf;
    --art-red: #e8442f;
  }
  * { box-sizing: border-box; margin: 0; padding: 0; }
  html, body { width: 1200px; height: 890px; overflow: hidden; }
  body { background: var(--stage); position: relative; font-family: "Arimo", Arial, sans-serif; }

  .cover {
    position: absolute; top: 115px; width: 440px; height: 660px;
    background: var(--paper);
    box-shadow: 0 14px 40px rgba(0,0,0,0.45);
  }
  .cover--front { left: 120px; }
  .cover--back { left: 640px; }

  /* Front */
  .front-title {
    margin-top: 38px; text-align: center;
    font-family: "Tinos", "Times New Roman", serif; font-weight: 700;
    color: var(--title-blue); font-size: 46px; line-height: 1.12; letter-spacing: 0.5px;
  }
  .front-art {
    display: block; margin: 22px auto 0; width: 330px; height: 250px; border-radius: 16px;
    background: linear-gradient(160deg, var(--art-red) 0%, var(--art-silver) 28%, var(--art-silver) 62%, var(--art-mint) 100%);
    opacity: 0.85;
  }
  .front-author {
    margin-top: 30px; text-align: center;
    font-family: "Cinzel", Georgia, serif; font-weight: 500;
    color: var(--author-teal); font-size: 36px; letter-spacing: 3px;
  }
  .front-url {
    margin-top: 4px; text-align: center;
    font-size: 11.5px; letter-spacing: 2.4px; color: var(--ink);
  }

  /* Back */
  .benefits { list-style: none; margin: 56px 0 0 48px; font-size: 15px; line-height: 1.4; color: var(--ink); }
  .benefits li { display: flex; align-items: center; gap: 10px; }
  .benefits svg { width: 10px; height: 10px; flex: none; }
  .benefits strong { font-weight: 700; }
  .back-url { margin: 24px 0 0 48px; font-size: 14px; letter-spacing: 3.2px; color: var(--link-teal); }

  .bio { display: flex; gap: 22px; margin: 34px 26px 0 40px; }
  .bio-photo { width: 108px; height: 108px; flex: none; background: var(--photo-teal); }
  .bio-text { font-size: 12px; line-height: 1.3; color: var(--ink); }
  .bio-text p + p { margin-top: 14px; }
  .bio-text strong { font-weight: 700; }

  .back-rule { height: 2px; background: var(--rule-blue); margin: 18px 34px 0 40px; }
  .availability { margin-top: 16px; text-align: center; font-size: 12px; line-height: 1.4; color: var(--ink); }
  .availability strong { color: var(--link-teal); font-weight: 700; }

  .brand { display: flex; align-items: center; gap: 8px; margin: 26px 0 0 40px; }
  .brand-dot { width: 22px; height: 22px; border-radius: 50%; background: var(--link-teal); }
  .brand-name { font-size: 16px; font-weight: 400; color: var(--link-teal); letter-spacing: 1.5px; }
</style>
</head>
<body>

<section class="cover cover--front">
  <h1 class="front-title">YOUR<br>GOLDEN YEARS<br>START<br>TOMORROW!</h1>
  <div class="front-art" role="img" aria-label="Illustration of a vintage silver camper trailer with red and white awnings, two mint lawn chairs and a pot of sunflowers"></div>
  <p class="front-author">MARK DELVORTH</p>
  <p class="front-url">www.goldenpathplanning.com</p>
</section>

<section class="cover cover--back">
  <ul class="benefits">
    <li><svg viewBox="0 0 10 10"><path d="M1 5.5 L4 8.5 L9 1.5" fill="none" stroke="#1a1a1a" stroke-width="1.8"/></svg><span><strong>REDUCE</strong> income taxes</span></li>
    <li><svg viewBox="0 0 10 10"><path d="M1 5.5 L4 8.5 L9 1.5" fill="none" stroke="#1a1a1a" stroke-width="1.8"/></svg><span><strong>ELIMINATE</strong> Social Security taxes</span></li>
    <li><svg viewBox="0 0 10 10"><path d="M1 5.5 L4 8.5 L9 1.5" fill="none" stroke="#1a1a1a" stroke-width="1.8"/></svg><span><strong>AVOID</strong> huge Medicare premium increase</span></li>
    <li><svg viewBox="0 0 10 10"><path d="M1 5.5 L4 8.5 L9 1.5" fill="none" stroke="#1a1a1a" stroke-width="1.8"/></svg><span><strong>LEAVE</strong> a tax-free legacy</span></li>
  </ul>
  <p class="back-url">www.goldenpathplanning.com</p>

  <div class="bio">
    <div class="bio-photo" role="img" aria-label="Portrait photo of the author"></div>
    <div class="bio-text">
      <p>Mark Delvorth is a <strong>CERTIFIED FINANCIAL PLANNER</strong> and holds a Master’s degree in Personal Financial Planning.</p>
      <p>Mark has provided financial advice to clients since 1998. over those 2 decades he has developed extensive knowledge of investment management, Social Security, tax, retirement planning and wealth transfer strategies.</p>
      <p>He has learned that succesful financial planning does not need to be complex. He follows the tried and true rule he learned in the Army, “Keep it Simple Stupid”</p>
    </div>
  </div>

  <div class="back-rule"></div>
  <p class="availability"><strong>Steady Money Planning</strong> is available at<br>www.goldenpathplanning.com<br>or by emailing mark@goldenpathplanning.com</p>

  <div class="brand">
    <span class="brand-dot"></span>
    <span class="brand-name">GOLDENPATH PLANNING</span>
  </div>
</section>

</body>
</html>
```